Uitnodiging van het huwelijk
doelgroep
Uitnodiging voor onze bruiloft voor vrienden en familie
Conceptuele formulering
Wij willen hutten individuele uitnodigingskaart. Het moet iets bijzonders zijn, dwz straalt iets bijzonders, maar anders vrij eenvoudig en modern en niet cheesy! Op de voorkant van onze huwelijksdatum en onze namen moeten eventueel een foto van ons. misschien zelfs een citaat: "Het geluk is het enige dat verdubbelt als je het (Gustav Mellinger) Uitnodiging voor onze kerk bruiloft misschien een motief, wat doe je het citaat past delen ....

```html
<!DOCTYPE html>
<html lang="de">
<head>
<meta charset="utf-8">
<title>Hochzeitseinladung</title>
<link rel="stylesheet" href="https://fonts.googleapis.com/css2?family=Great+Vibes&family=Italianno&family=Open+Sans:wght@400&display=swap">
<style>
  :root {
    --page: #ffffff;
    --card-edge: #222222;
    --card-edge-soft: #9a9a9a;
    --quote: #c41c58;
    --headline: #e0392b;
    --script-grey: #4a4a4a;
    --body: #333333;
    --heart-pink: #ea87a9;
    --heart-peach: #f4a68a;
  }
  * { box-sizing: border-box; margin: 0; padding: 0; }
  html, body {
    width: 1183px; height: 1200px; overflow: hidden;
    background: var(--page);
  }
  .stage { position: relative; width: 1183px; height: 1200px; }

  .card {
    position: absolute; left: 18px; width: 1147px;
    background: var(--page);
  }
  .card--outside { top: 14px; height: 573px; border: 1.5px solid var(--card-edge); }
  .card--inside { top: 618px; height: 575px; border: 1.5px solid var(--card-edge-soft); }

  .quote {
    position: absolute; left: 100px; top: 76px; width: 366px;
    text-align: center;
    font-family: "Italianno", cursive;
    font-size: 34px; line-height: 42px;
    color: var(--quote);
  }
  .quote__author {
    display: block; margin-top: 0;
    font-style: normal;
    font-size: 17px; line-height: 20px;
    color: var(--script-grey);
  }

  .motif {
    position: absolute;
    background: radial-gradient(ellipse at center,
      rgba(234,135,169,0.85) 0%, rgba(244,166,138,0.7) 45%, rgba(244,166,138,0) 72%);
  }
  .motif--pair { left: 660px; top: 62px; width: 400px; height: 390px; }
  .motif--scatter { left: 20px; top: 255px; width: 230px; height: 300px;
    background: radial-gradient(ellipse at center,
      rgba(244,166,138,0.6) 0%, rgba(234,135,169,0.35) 45%, rgba(244,166,138,0) 72%); }
  .motif--corner-left { left: 50px; top: 390px; width: 110px; height: 140px;
    background: radial-gradient(ellipse at center,
      rgba(244,166,138,0.55) 0%, rgba(244,166,138,0) 70%); }
  .motif--corner-right { left: 985px; top: 390px; width: 115px; height: 140px;
    background: radial-gradient(ellipse at center,
      rgba(244,166,138,0.55) 0%, rgba(244,166,138,0) 70%); }

  .yes {
    position: absolute; left: 970px; top: 392px;
    font-family: "Great Vibes", cursive;
    font-size: 96px; line-height: 1;
    color: var(--script-grey);
  }

  .couple {
    position: absolute; left: 110px; top: 62px; width: 360px;
    text-align: center;
    font-family: "Great Vibes", cursive; font-weight: 400;
    font-size: 92px; line-height: 112px;
    color: var(--script-grey);
  }

  .invitation {
    position: absolute; left: 600px; top: 62px; width: 520px;
    text-align: center;
  }
  .invitation__headline {
    font-family: "Great Vibes", cursive; font-weight: 400;
    font-size: 54px; line-height: 70px;
    color: var(--headline);
  }
  .invitation__text {
    margin-top: 14px;
    font-family: "Open Sans", sans-serif;
    font-size: 16.5px; line-height: 23px;
    color: var(--body);
  }
  .invitation__text p + p { margin-top: 23px; }
</style>
</head>
<body>
<main class="stage">
  <section class="card card--outside" aria-label="Außenseite der Karte">
    <blockquote class="quote">
      Das Glück ist das einzige,<br>
      das sich verdoppelt,<br>
      wenn man es teilt.
      <cite class="quote__author">Gustav Mellinger</cite>
    </blockquote>
    <div class="motif motif--scatter" role="img" aria-label="Verstreute kleine Herzen in Rosa und Apricot"></div>
    <div class="motif motif--pair" role="img" aria-label="Zwei große, sich überlappende Herzen in Rosa und Apricot"></div>
    <p class="yes">ja!</p>
  </section>

  <section class="card card--inside" aria-label="Innenseite der Karte">
    <h1 class="couple">Name<br>&amp;<br>Name</h1>
    <div class="motif motif--corner-left" role="img" aria-label="Kleine Herzen in der Ecke"></div>
    <div class="invitation">
      <h2 class="invitation__headline">Wir trauen uns!<br>Am 11. Mustermonat 1111</h2>
      <div class="invitation__text">
        <p>Zu diesem besonderen Tag seid Ihr<br>ganz herzlich eingeladen!</p>
        <p>Die kirchliche Trauung findet um 11:11 Uhr<br>in der Musterkirche, Musterstraße 1,<br>12345 Musterhausen statt.</p>
        <p>Anschließend feiern wir im<br>Musterrestaurant,<br>Musterstraße 1, 12345 Musterstadt.</p>
        <p>Wir freuen uns sehr auf Euch!</p>
      </div>
    </div>
    <div class="motif motif--corner-right" role="img" aria-label="Kleine Herzen in der Ecke"></div>
  </section>
</main>
</body>
</html>
```